Postcard Design/Coupon

My business is a Pizza Shop/Restaurant/Bar. I know confusing. I sell mainly pizza and beer but sandwich's and salads are a big seller also. So I want coupons/postcards that I can hand out to every table that comes in to entice them to come back. I also will be sending these coupons/postcards to delivery customers. The business name is Larkdale Pizza Vento address is 581 Thistle Avenue Brookmere PA15990 phone number is 412-741-1744On one side I wanted the coupon offer and logo and the other side the hours but also room for me to send some out.

Target Market(s)

Families

Industry/Entity Type

Restaurant

Requirements
Must have
• Pizza
Nice to have
• Salads/Hoagies/Nice Description

```html
<!DOCTYPE html>
<html lang="en">
<head>
<meta charset="utf-8">
<title>Larkdale Pizza Vento – Postcard Back</title>
<link rel="stylesheet" href="https://fonts.googleapis.com/css2?family=Archivo+Black&display=swap">
<style>
  :root {
    --paper: #ffffff;
    --ink: #111111;
    --frame: #222222;
    --orange: #f7931e;
    --red: #b22430;
    --yellow: #ffe81a;
    --rule: #333333;
    --photo-amber: #e8a33a;
    --photo-cream: #f3e2bf;
    --photo-green: #9bbf5a;
  }
  html, body {
    margin: 0;
    padding: 0;
    width: 1200px;
    height: 930px;
    overflow: hidden;
    background: var(--paper);
  }
  .postcard {
    position: relative;
    width: 1200px;
    height: 930px;
    box-sizing: border-box;
    border: 1px solid var(--frame);
    background: var(--paper);
    font-family: "Archivo Black", "Arial Black", sans-serif;
    color: var(--ink);
    overflow: hidden;
  }
  .food-photo {
    position: absolute;
    left: 60px;
    top: 45px;
    width: 405px;
    height: 295px;
    border-radius: 40px 60px 30px 20px;
    background: linear-gradient(100deg, var(--photo-amber) 0%, var(--photo-amber) 30%, var(--photo-cream) 55%, var(--photo-green) 100%);
  }
  .brand-name {
    position: absolute;
    left: 460px;
    top: 70px;
    width: 250px;
    margin: 0;
    text-align: center;
    font-size: 34px;
    line-height: 40px;
    font-weight: 400;
    color: var(--ink);
  }
  .stamp-box {
    position: absolute;
    left: 1055px;
    top: 50px;
    width: 96px;
    height: 138px;
    box-sizing: border-box;
    border: 1.5px solid var(--frame);
  }
  .hours-panel {
    position: absolute;
    left: 0;
    top: 345px;
    width: 580px;
    height: 458px;
    background: var(--orange);
  }
  .hours-group {
    position: absolute;
    left: 50px;
    margin: 0;
    font-size: 20.8px;
    line-height: 25.3px;
    white-space: nowrap;
  }
  .hours-group h2 {
    margin: 0;
    font-size: 25.5px;
    line-height: 29px;
    font-weight: 400;
    color: var(--paper);
    letter-spacing: 0.3px;
  }
  .hours-group p { margin: 0; }
  .hours-lounge { top: 27px; }
  .hours-kitchen { top: 135px; }
  .hours-dining { top: 267px; }
  .contact-band {
    position: absolute;
    left: 0;
    top: 803px;
    width: 580px;
    height: 127px;
    background: var(--red);
    color: var(--yellow);
  }
  .contact-address {
    position: absolute;
    left: 50px;
    top: 16px;
    margin: 0;
    font-size: 21.5px;
    white-space: nowrap;
  }
  .contact-phone {
    position: absolute;
    left: 49px;
    top: 38px;
    margin: 0;
    font-size: 38px;
    letter-spacing: 0.5px;
  }
  .address-lines {
    position: absolute;
    left: 0;
    top: 0;
  }
</style>
</head>
<body>
  <main class="postcard">
    <div class="food-photo" role="img" aria-label="Photo of a foamy mug of beer beside an Italian hoagie"></div>

    <h1 class="brand-name">Larkdale<br>Pizza<br>Vento</h1>

    <div class="stamp-box" aria-label="Stamp area"></div>

    <section class="hours-panel">
      <div class="hours-group hours-lounge">
        <h2>LOUNGE:</h2>
        <p>Monday through Saturday 11am to 2am</p>
        <p>Sunday Noon to 2am</p>
      </div>
      <div class="hours-group hours-kitchen">
        <h2>KITCHEN:</h2>
        <p>Monday through Thursday 11am to11pm</p>
        <p>Friday and Saturday 11am to midnight</p>
        <p>Sunday Noon to 10</p>
      </div>
      <div class="hours-group hours-dining">
        <h2>DINING ROOM:</h2>
        <p>Closed Monday</p>
        <p>Tuesday through Thursday 11am to10pm</p>
        <p>Friday and Saturday 11am to 11pm</p>
        <p>Sunday Noon to 9pm</p>
        <p>Call for Delivery hours</p>
      </div>
    </section>

    <section class="contact-band">
      <p class="contact-address">581 Thistle Avenue Brookmere PA15990</p>
      <p class="contact-phone">412-555-0187</p>
    </section>

    <svg class="address-lines" width="1200" height="930" aria-hidden="true">
      <g stroke="var(--rule)" stroke-width="1.3">
        <line x1="700" y1="519.5" x2="1151" y2="519.5"/>
        <line x1="700" y1="617.5" x2="1151" y2="617.5"/>
        <line x1="700" y1="714.5" x2="1151" y2="714.5"/>
        <line x1="900" y1="811.5" x2="1151" y2="811.5"/>
      </g>
    </svg>
  </main>
</body>
</html>
```